Mrs Pellow's Menu Design

Our website is MrsPellows.com.au
Please take inspiration in the look and feel, style and tone from the photos of our takeaway restaurant.

We' have been providing our famous Chinese take away in Merrylands for over 30 years. We have seen the neighbourhood grow around us and we have grown along with them.
We have had a recent shopfitting (see photos on http://www.mrspellows.com.au).

Red features prominently in our shop design but understand if you would keep it muted or minimal for readability.

We would like to revamp our plain menu to a fresh new look with a typeface that emphasizes familiarity and simple, delicious food.
Updates

Reason: Updated brief with more information Would like more designs

Target Market(s)

Our customers are locals who have enjoyed our famous Chinese takeaway for over 30 years. They are mums buying takeout for their family dinner, staff from the surrounding mall shops after a quick, delicious feed and regulars who come in every week for their fix of freshly prepared, familiar Chinese favourites like san choy bow, crispy salt and pepper squid and stir-fried beef in black bean sauce.

Industry/Entity Type

Shop

Requirements
Must have
• Typeface is very important.
It must be readable and convey a classic Chinese menu that oozes familiarity and sincerity. We serve simple, classic Chinese favorites at a economical price
Should not have
• Should not be childish, cartoony or cliched.

```html
<!DOCTYPE html>
<html lang="en">
<head>
<meta charset="utf-8">
<title>Mrs Pellow's Menu</title>
<link href="https://fonts.googleapis.com/css2?family=Roboto+Condensed:wght@400;700&display=swap" rel="stylesheet">
<style>
:root{
  --red:#e41e26;
  --ink:#231f20;
  --paper:#f1f1f1;
  --panel:#ffffff;
  --rule:#cfcfcf;
  --caption:#9b9b9b;
  --map:#5f6a72;
}
*{margin:0;padding:0;box-sizing:border-box}
html,body{width:1200px;height:849px;overflow:hidden;background:var(--panel)}
body{position:relative;font-family:"Roboto Condensed",Arial Narrow,sans-serif;color:var(--ink)}
.page{position:absolute;top:0;width:400px;height:849px;background:var(--paper)}
.page--left{left:0;border-right:1px solid var(--rule)}
.page--middle{left:400px;border-right:1px solid var(--rule)}
.block{position:absolute}
.section-head{position:absolute;height:17px}
.section-head .bar{position:absolute;top:0;height:17px;background:var(--red);color:#fff;font-weight:700;font-size:13px;letter-spacing:1.5px;text-align:center;line-height:17px}
.section-head .mark{position:absolute;top:1px;width:15px;height:15px;background:var(--red)}
.menu{list-style:none;position:absolute}
.menu li{display:flex;align-items:flex-end;height:17px;font-size:12px;line-height:14px}
.menu .name{white-space:nowrap}
.menu .name small{font-size:10px}
.menu .lead{flex:1;border-bottom:1px dotted var(--ink);margin:0 3px 3px}
.menu .price{white-space:nowrap}
.menu .icon{width:12px;height:12px;margin-right:2px;flex:none;align-self:center}
.banner{position:absolute;height:16px;background:var(--red);color:#fff;font-weight:700;font-size:11px;line-height:16px;text-align:center}
.banner-mark{position:absolute;width:14px;height:14px;background:var(--red)}
.map{position:absolute;left:425px;top:437px;width:345px;height:258px;background:linear-gradient(#5f6a72,#6d7780);border-radius:2px}
.notes{position:absolute;left:485px;top:730px;width:230px;list-style:none;text-align:center;font-size:11px;font-weight:700}
.notes li{height:25px;padding-top:1px;border-bottom:1px solid var(--ink);margin-bottom:0}
.notes li:last-child{border-bottom:none}
.preview{position:absolute;left:800px;top:0;width:400px;height:435px;background:var(--paper)}
.preview .mark{position:absolute;left:85px;top:30px;width:45px;height:45px;background:var(--red)}
.preview .bar{position:absolute;left:175px;top:30px;right:0;height:45px;background:var(--red)}
.preview-list{list-style:none;position:absolute;left:36px;top:86px}
.preview-list li{display:flex;align-items:center;height:43.4px;font-size:32px;white-space:nowrap}
.preview-list svg{width:38px;height:38px;margin-right:10px;flex:none}
.caption{position:absolute;left:851px;top:440px;font-size:30px;color:var(--caption)}
</style>
</head>
<body>
<svg width="0" height="0" style="position:absolute" aria-hidden="true">
  <defs>
    <symbol id="i-thumb" viewBox="0 0 40 40"><circle cx="20" cy="20" r="20" fill="#231f20"/><path d="M13 18h5l3-7c2 0 3 1 3 3l-1 4h5c2 0 3 2 2 3l-2 8c0 1-1 2-3 2H13z" fill="#fff"/></symbol>
    <symbol id="i-chili" viewBox="0 0 40 40"><circle cx="20" cy="20" r="20" fill="#231f20"/><path d="M11 29c8-1 14-7 16-15l3 2c-2 9-9 15-19 14z" fill="#fff"/><path d="M27 14l2-4" stroke="#fff" stroke-width="2"/></symbol>
    <symbol id="i-cloche" viewBox="0 0 40 40"><circle cx="20" cy="20" r="20" fill="#231f20"/><path d="M10 25a10 10 0 0 1 20 0z" fill="#fff"/><rect x="8" y="27" width="24" height="2" fill="#fff"/><circle cx="20" cy="13" r="2" fill="#fff"/></symbol>
    <symbol id="i-dish" viewBox="0 0 40 40"><circle cx="20" cy="20" r="20" fill="#231f20"/><rect x="9" y="20" width="22" height="9" fill="#fff"/><path d="M15 17c0-3 2-3 2-6M20 17c0-3 2-3 2-6M25 17c0-3 2-3 2-6" stroke="#fff" stroke-width="1.5" fill="none"/></symbol>
  </defs>
</svg>

<section class="page page--left">
  <div class="section-head" style="left:0;top:28px;width:400px">
    <span class="mark" style="left:32px"></span><span class="bar" style="left:60px;width:270px">OMELETTE</span><span class="mark" style="left:337px"></span>
  </div>
  <ul class="menu" style="left:18px;top:48px;width:347px">
    <li><svg class="icon"><use href="#i-thumb"/></svg><span class="name">Plain Omelette</span><span class="lead"></span><span class="price">$6.90</span></li>
    <li><svg class="icon"><use href="#i-chili"/></svg><span class="name">Prawn Omelette</span><span class="lead"></span><span class="price">$8.00</span></li>
    <li><svg class="icon"><use href="#i-cloche"/></svg><span class="name">Chicken Omelette</span><span class="lead"></span><span class="price">$8.00</span></li>
    <li><svg class="icon"><use href="#i-dish"/></svg><span class="name">Combination Omelette</span><span class="lead"></span><span class="price">$8.00</span></li>
    <li><svg class="icon"><use href="#i-thumb"/></svg><span class="name">Vegetable Omelette</span><span class="lead"></span><span class="price">$8.00</span></li>
    <li><svg class="icon"><use href="#i-chili"/></svg><span class="name">BBQ Pork Omelette</span><span class="lead"></span><span class="price">$8.00</span></li>
    <li><svg class="icon"><use href="#i-cloche"/></svg><span class="name">Beef Omelette</span><span class="lead"></span><span class="price">$9.00</span></li>
    <li><svg class="icon"><use href="#i-dish"/></svg><span class="name">King Prawn Omelette</span><span class="lead"></span><span class="price">$9.50</span></li>
  </ul>
  <ul class="menu" style="left:34px;top:184px;width:331px">
    <li><span class="name">Chow Mein <small>(Served with Crispy Noodles)</small></span><span class="lead" style="margin-right:40px"></span></li>
    <li><span class="name">Stir Fried Mixed Vegetable Chow Mein</span><span class="lead"></span><span class="price">$7.50</span></li>
    <li><span class="name">Prawn Chow Mein</span><span class="lead"></span><span class="price">$8.00</span></li>
    <li><span class="name">Chicken Chow Mein</span><span class="lead"></span><span class="price">$8.00</span></li>
    <li><span class="name">Beef Chow Mein</span><span class="lead"></span><span class="price">$9.30</span></li>
    <li><span class="name">Braised Chicken Chow Mein</span><span class="lead"></span><span class="price">$9.30</span></li>
    <li><span class="name">Sliced Pork Chow Mein</span><span class="lead"></span><span class="price">$9.30</span></li>
    <li><span class="name">Combination Chow Mein</span><span class="lead"></span><span class="price">$9.80</span></li>
    <li><span class="name">King Prawn Chow Mein</span><span class="lead"></span><span class="price">$10.40</span></li>
    <li><span class="name">Seafood Chow Mein</span><span class="lead"></span><span class="price">$12.00</span></li>
  </ul>

  <div class="section-head" style="left:0;top:352px;width:400px">
    <span class="mark" style="left:32px"></span><span class="bar" style="left:60px;width:270px">RICE</span><span class="mark" style="left:337px"></span>
  </div>
  <ul class="menu" style="left:34px;top:372px;width:331px">
    <li><span class="name">Small Fried Rice</span><span class="lead"></span><span class="price">$5.00</span></li>
    <li><span class="name">Large Fried Rice</span><span class="lead"></span><span class="price">$6.00</span></li>
    <li><span class="name">Vegetarian Fried Rice</span><span class="lead"></span><span class="price">$6.00</span></li>
    <li><span class="name">Chicken Fried Rice</span><span class="lead"></span><span class="price">$7.50</span></li>
    <li><span class="name">Curried Prawns and Rice</span><span class="lead"></span><span class="price">$8.00</span></li>
    <li><span class="name">Curried Chicken and Rice</span><span class="lead"></span><span class="price">$8.00</span></li>
    <li><span class="name">Special Fried Rice</span><span class="lead"></span><span class="price">$8.50</span></li>
    <li><span class="name">Boiled Rice <small>(Small)</small></span><span class="lead"></span><span class="price">$2.50</span></li>
    <li><span class="name">Boiled Rice <small>(Large)</small></span><span class="lead"></span><span class="price">$3.00</span></li>
  </ul>

  <div class="section-head" style="left:0;top:527px;width:400px">
    <span class="mark" style="left:32px"></span><span class="bar" style="left:60px;width:270px">THICK RICE NOODLES</span><span class="mark" style="left:337px"></span>
  </div>
  <ul class="menu" style="left:34px;top:547px;width:331px">
    <li><span class="name">Soya Sauce Beef with Thick Rice Noodles</span><span class="lead"></span><span class="price">$10.00</span></li>
    <li><span class="name">Beef in Scrambled Egg with Thick Rice Noodles</span><span class="lead"></span><span class="price">$10.30</span></li>
    <li><span class="name">Beef &amp; Black Bean Sauce with Thick Rice Noodles</span><span class="lead"></span><span class="price">$10.30</span></li>
    <li><span class="name">Braised Chicken with Thick Rice Noodles</span><span class="lead"></span><span class="price">$10.30</span></li>
    <li><span class="name">Beef and Vegetables with Thick Rice Noodles</span><span class="lead"></span><span class="price">$10.30</span></li>
    <li><span class="name">Combination Thick Rice Noodles</span><span class="lead"></span><span class="price">$11.30</span></li>
    <li><span class="name">Sate Chicken with Thick Rice Noodles</span><span class="lead"></span><span class="price">$11.40</span></li>
    <li><span class="name">King Prawn in Scrambled Egg with Thick Rice Noodles</span><span class="lead"></span><span class="price">$11.40</span></li>
    <li><span class="name">Lamb and Black Pepper Sauce with Thick Rice Noodles</span><span class="lead"></span><span class="price">$12.30</span></li>
  </ul>

  <div class="section-head" style="left:0;top:702px;width:400px">
    <span class="mark" style="left:32px"></span><span class="bar" style="left:60px;width:270px">LAKSA</span><span class="mark" style="left:337px"></span>
  </div>
  <ul class="menu" style="left:34px;top:722px;width:331px">
    <li><span class="name">Vegetable Laksa</span><span class="lead"></span><span class="price">$9.50</span></li>
    <li><span class="name">Beef Laksa</span><span class="lead"></span><span class="price">$10.00</span></li>
    <li><span class="name">Braised Chicken Laksa</span><span class="lead"></span><span class="price">$10.00</span></li>
    <li><span class="name">Combination Laksa</span><span class="lead"></span><span class="price">$10.00</span></li>
    <li><span class="name">King Prawn Laksa</span><span class="lead"></span><span class="price">$10.80</span></li>
    <li><span class="name">Seafood Laksa</span><span class="lead"></span><span class="price">$12.00</span></li>
  </ul>
</section>

<section class="page page--middle">
  <div class="section-head" style="left:0;top:28px;width:400px">
    <span class="mark" style="left:32px"></span><span class="bar" style="left:67px;width:245px">LUNCH SPECIAL <span style="font-weight:400;letter-spacing:0">(10am-3pm)</span></span><span class="mark" style="left:334px"></span>
  </div>
  <ul class="menu" style="left:34px;top:48px;width:331px">
    <li><span class="name">Small Prawns &amp; Vegetables</span><span class="lead"></span><span class="price">$6.00</span></li>
    <li><span class="name">Curry Prawns</span><span class="lead"></span><span class="price">$6.00</span></li>
    <li><span class="name">Sweet &amp; Sour Chicken</span><span class="lead"></span><span class="price">$6.00</span></li>
    <li><span class="name">Chicken &amp; Vegetables</span><span class="lead"></span><span class="price">$6.00</span></li>
    <li><span class="name">Curry Chicken</span><span class="lead"></span><span class="price">$6.00</span></li>
    <li><span class="name">Sweet &amp; Sour Pork</span><span class="lead"></span><span class="price">$6.00</span></li>
    <li><span class="name">Mixed Vegetables</span><span class="lead"></span><span class="price">$6.00</span></li>
    <li><span class="name">Honey King Prawns</span><span class="lead"></span><span class="price">$6.50</span></li>
    <li><span class="name">Beef with Black Bean Sauce</span><span class="lead"></span><span class="price">$6.50</span></li>
    <li><span class="name">Honey Chicken <small>(Boneless)</small></span><span class="lead"></span><span class="price">$6.50</span></li>
    <li><span class="name">Lemon Chicken <small>(Boneless)</small></span><span class="lead"></span><span class="price">$6.50</span></li>
    <li><span class="name">Deep Fried Lamb with Special Sauce</span><span class="lead"></span><span class="price">$6.50</span></li>
    <li><span class="name">Mongolian Beef</span><span class="lead"></span><span class="price">$7.30</span></li>
    <li><span class="name">Beef with Sate Sauce</span><span class="lead"></span><span class="price">$7.30</span></li>
    <li><span class="name">Beef with Chilli Sauce</span><span class="lead"></span><span class="price">$7.30</span></li>
    <li><span class="name">Braised Chicken with Sate Sauce</span><span class="lead"></span><span class="price">$7.30</span></li>
    <li><span class="name">Braised Chicken with Chilli Sauce</span><span class="lead"></span><span class="price">$7.30</span></li>
    <li><span class="name">Mongolian Lamb</span><span class="lead"></span><span class="price">$7.30</span></li>
  </ul>

  <span class="banner-mark" style="left:32px;top:379px"></span>
  <div class="banner" style="left:68px;top:378px;width:267px">ALL DISHES SERVED WITH: FRIED RICE BOILED RICE</div>
  <div class="banner" style="left:66px;top:398px;width:266px">SOFT NOODLES OR THICK RICE NOODLES $1.50 EXTRA</div>
  <span class="banner-mark" style="left:337px;top:399px"></span>
</section>

<div class="map" role="img" aria-label="Street map showing Mrs Pellow's Chinese Kitchen inside the shopping mall, with surrounding streets, parking and the council car park"></div>

<ul class="notes">
  <li>ALL PRICES GST INCLUSIVE</li>
  <li>PRICES SUBJECT TO CHANGE WITHOUT NOTICE</li>
  <li>ALL MEALS CONTAIN SMALL QUANTITIES OF MSG</li>
</ul>

<section class="preview">
  <span class="mark"></span><span class="bar"></span>
  <ul class="preview-list">
    <li><svg><use href="#i-thumb"/></svg>Plain Omelette.............</li>
    <li><svg><use href="#i-chili"/></svg>Prawn Omelette.............</li>
    <li><svg><use href="#i-cloche"/></svg>Chicken Omelette..........</li>
    <li><svg><use href="#i-dish"/></svg>Combination Omelette....</li>
    <li><svg><use href="#i-thumb"/></svg>Vegetable Omelette.........</li>
    <li><svg><use href="#i-chili"/></svg>BBQ Pork Omelette.........</li>
    <li><svg><use href="#i-cloche"/></svg>Beef Omelette................</li>
    <li><svg><use href="#i-dish"/></svg>King Prawn Omelette......</li>
  </ul>
</section>
<p class="caption">big preview of icons</p>
</body>
</html>
```